Maple Lantern Business Card

Design of business cards

Target Market(s)

We are aiming as small business owners who need anything from basic business structures, website plans, business processes and quality assurance.

Industry/Entity Type

Business

Colors

Designer to choose colors to be used in the design.

Requirements
Nice to have
• I would prefer one side of the card to use the green from the logo. Prefer to have the same font as the logo.

```html
<!DOCTYPE html>
<html lang="en">
<head>
<meta charset="utf-8">
<title>Maple Lantern Consulting – Business Card</title>
<link href="https://fonts.googleapis.com/css2?family=Cinzel:wght@400;600;700&display=swap" rel="stylesheet">
<style>
  :root {
    --lime: #a8cd3a;
    --charcoal: #58585a;
    --paper: #ffffff;
    --backdrop: #cfcfcf;
    --ink: #555557;
  }
  html, body {
    margin: 0;
    padding: 0;
    width: 900px;
    height: 1200px;
    overflow: hidden;
    background: var(--backdrop);
  }
  .canvas {
    position: relative;
    width: 900px;
    height: 1200px;
    font-family: "Cinzel", "Trajan Pro", serif;
  }
  .card {
    position: absolute;
    box-sizing: border-box;
  }
  /* Front side */
  .card--front {
    left: 148px;
    top: 168px;
    width: 572px;
    height: 337px;
    background: var(--lime);
  }
  .card--front .edge-stripe {
    position: absolute;
    left: 0;
    top: 0;
    width: 12px;
    height: 100%;
    background: var(--charcoal);
  }
  .brand {
    position: absolute;
    display: flex;
    align-items: center;
  }
  .brand__square {
    flex: none;
  }
  .brand__name {
    margin: 0;
    font-weight: 600;
    line-height: 1.3;
  }
  .card--front .brand {
    left: 104px;
    top: 118px;
    gap: 26px;
  }
  .card--front .brand__square {
    width: 62px;
    height: 62px;
    background: var(--paper);
  }
  .card--front .brand__name {
    font-size: 22px;
    color: var(--paper);
  }
  /* Back side */
  .card--back {
    left: 148px;
    top: 690px;
    width: 575px;
    height: 337px;
    background: var(--paper);
  }
  .card--back .brand {
    left: 44px;
    top: 50px;
    gap: 20px;
  }
  .card--back .brand__square {
    width: 46px;
    height: 46px;
    background: var(--lime);
  }
  .card--back .brand__name {
    font-size: 17px;
    color: var(--lime);
  }
  .contact {
    position: absolute;
    left: 322px;
    top: 230px;
    margin: 0;
    font-size: 12px;
    font-weight: 700;
    color: var(--ink);
    letter-spacing: 0.5px;
    line-height: 25px;
  }
  .contact p { margin: 0; }
  .bottom-band {
    position: absolute;
    left: 0;
    bottom: 0;
    width: 100%;
    height: 12px;
    display: flex;
  }
  .bottom-band__dark { width: 372px; background: var(--charcoal); }
  .bottom-band__lime { flex: 1; background: var(--lime); }
</style>
</head>
<body>
  <main class="canvas">
    <section class="card card--front" aria-label="Card front">
      <div class="edge-stripe"></div>
      <div class="brand">
        <span class="brand__square"></span>
        <h1 class="brand__name">Maple Lantern<br>Consulting</h1>
      </div>
    </section>

    <section class="card card--back" aria-label="Card back">
      <div class="brand">
        <span class="brand__square"></span>
        <h2 class="brand__name">Maple Lantern<br>Consulting</h2>
      </div>
      <div class="contact">
        <p>Name -</p>
        <p>Mobile-</p>
      </div>
      <div class="bottom-band">
        <span class="bottom-band__dark"></span>
        <span class="bottom-band__lime"></span>
      </div>
    </section>
  </main>
</body>
</html>
```